Brolvane Co.,Ltd. need business card

Brolvane Company Limited is a facility management company. We provides a total solution services from administration, energy saving, security, safety, food catering to companies.

The logo should be in elegant style with innovative that suited to the upper market
Please see the logo image in the attached file. You can use this Red or Blue or Green checkerboard (color and font should be similar to logo) as the main part of business card (can be an entire of one side of business card) . In another side of card should contain contact details of personnel - here below demo information

Kanyarat Thoengsai
Chief Executive Officer

No.73, Soi 5, Ruam Wongsa Road
Nong Khaem, Bangkok,
10520, Thailand

Tel + 66841537296
Mobile + 66841537296
E-mail: Kanyarat.Thoengsai@brolvane-example.co.th

Target Market(s)

Factory, Hotel and Hospital

Industry/Entity Type

Business

Contact Information for Business Card

Kanyarat Thoengsai
Chief Executive Officer

Nong Khaem, Bangkok,
10520, Thailand

Tel + 66841537296
Mobile + 66841537296

We will change details with the winner designer

Font styles to use
Sans Serif

Requirements
Must have
• In style of red checkerboard and white color

```html
<!DOCTYPE html>
<html lang="en">
<head>
<meta charset="utf-8">
<title>Brolvane Co.,Ltd. – Business Card</title>
<link rel="stylesheet" href="https://fonts.googleapis.com/css2?family=Open+Sans:wght@400;600;700&display=swap">
<style>
  :root {
    --page-bg: #e9e7e3;
    --paper-white: #f6f6f6;
    --band-black: #0b0b0e;
    --brand-blue: #3732c2;
    --brand-blue-deep: #2620a6;
    --brand-blue-light: #4842d6;
    --text-white: #ffffff;
    --logo-blue: #3a34c4;
  }
  * { box-sizing: border-box; margin: 0; padding: 0; }
  html, body { width: 1200px; height: 780px; overflow: hidden; }
  body {
    background: var(--page-bg);
    font-family: "Open Sans", Arial, sans-serif;
    display: flex;
    align-items: center;
    justify-content: center;
    gap: 56px;
  }
  .card {
    width: 540px;
    height: 309px;
    border-radius: 16px;
    overflow: hidden;
    position: relative;
    box-shadow: 0 6px 18px rgba(0,0,0,0.18);
  }

  /* Front: contact side */
  .card-front { background: var(--brand-blue); display: flex; flex-direction: column; }
  .logo-panel {
    height: 132px;
    background: var(--paper-white);
    display: flex;
    align-items: center;
    justify-content: center;
  }
  .wordmark {
    font-family: "Open Sans", Arial, sans-serif;
    font-weight: 400;
    color: var(--logo-blue);
    letter-spacing: 0.22em;
    font-size: 52px;
    line-height: 1;
  }
  .divider-band { height: 18px; background: var(--band-black); }
  .contact-panel {
    flex: 1;
    background: linear-gradient(180deg, var(--brand-blue-light) 0%, var(--brand-blue) 45%, var(--brand-blue-deep) 100%);
    color: var(--text-white);
    padding: 10px 26px 0 26px;
  }
  .identity-line { font-size: 15px; display: flex; align-items: center; gap: 9px; }
  .person-name { font-weight: 700; text-transform: uppercase; letter-spacing: 0.01em; }
  .identity-sep { width: 1px; height: 17px; background: var(--text-white); }
  .person-title { font-size: 13px; font-weight: 400; }
  .details { display: flex; margin-top: 18px; gap: 14px; }
  .contact-lines { font-size: 11.5px; line-height: 1.55; text-align: right; }
  .contact-line { display: flex; justify-content: flex-end; align-items: center; gap: 5px; }
  .contact-icon { width: 12px; height: 12px; flex: none; }
  .details-rule { width: 1px; background: rgba(255,255,255,0.85); align-self: stretch; }
  .address { font-size: 12px; line-height: 1.45; }

  /* Back: brand side */
  .card-back { display: flex; align-items: center; justify-content: center; }
  .back-pattern {
    position: absolute; inset: 0;
    background: radial-gradient(ellipse at 50% 40%, var(--brand-blue-light) 0%, var(--brand-blue) 55%, var(--brand-blue-deep) 100%);
  }
  .card-back .wordmark { position: relative; color: var(--paper-white); font-size: 58px; }
</style>
</head>
<body>
  <section class="card card-front" aria-label="Business card, contact side">
    <div class="logo-panel"><span class="wordmark">BROLVANE</span></div>
    <div class="divider-band"></div>
    <div class="contact-panel">
      <p class="identity-line">
        <span class="person-name">Kanyarat Thoengsai</span>
        <span class="identity-sep"></span>
        <span class="person-title">Chief Executive Officer</span>
      </p>
      <div class="details">
        <div class="contact-lines">
          <p class="contact-line">+ 66841537296
            <svg class="contact-icon" viewBox="0 0 12 12" aria-label="Telephone"><rect width="12" height="12" fill="#fff"/><path d="M3 3.2c0-.4.3-.6.7-.6h1l.5 1.6-.7.6c.4.9 1 1.5 1.8 1.8l.6-.7 1.6.5v1c0 .4-.2.7-.6.7C5.3 8.1 3 5.8 3 3.2z" fill="#3732c2"/></svg>
          </p>
          <p class="contact-line">+ 66841537296
            <svg class="contact-icon" viewBox="0 0 12 12" aria-label="Mobile"><rect width="12" height="12" fill="#fff"/><rect x="4" y="2" width="4" height="8" rx="0.6" fill="#3732c2"/><rect x="4.6" y="3" width="2.8" height="5" fill="#fff"/></svg>
          </p>
          <p class="contact-line">Kanyarat.Thoengsai@brolvane-example.co.th
            <svg class="contact-icon" viewBox="0 0 12 12" aria-label="E-mail"><rect width="12" height="12" fill="#fff"/><rect x="2" y="3.5" width="8" height="5" fill="#3732c2"/><path d="M2 3.5l4 3 4-3" stroke="#fff" stroke-width="0.8" fill="none"/></svg>
          </p>
        </div>
        <div class="details-rule"></div>
        <address class="address" style="font-style:normal">
          No.73, Soi 5, Ruam Wongsa Road<br>
          Nong Khaem, Bangkok<br>
          10520, Thailand
        </address>
      </div>
    </div>
  </section>

  <section class="card card-back" aria-label="Business card, brand side">
    <div class="back-pattern" role="img" aria-label="Subtle blue checkerboard pattern"></div>
    <span class="wordmark">BROLVANE</span>
  </section>
</body>
</html>
```